The Molar Compass (Cover Design for Ebook)

I need a cool and exciting eBook cover for my new book, launching very soon!
I want it to stand out and appeal to young professionals with big dreams.
It should be dramatic and bold and avoid cliche or generic photos. Simple design will work as long as it relates to the message of the book. The content will provide ten years of experience from working in the field and achieving success.
Title: The Molar Compass (at the top)
(Subheading Updated) The secrets to money, motivation and success they don’t teach you in dental school
OR The secrets to success they don't teach you in dental school.
OR The secrets to money, motivation and success
(smaller under title)
Author Updated: Dr K Fenwick (place at the bottom)
Updates

Target Market(s)

Ambitious young dentists
See instagram www.snapreel.com/themolarcompass for a sense of the style that I think could work.

Font styles to use
Serif
Sans Serif

Colors

Designer to choose colors to be used in the design.

Requirements
Must have
• Eye catching and cool.
• Show the benefits of success. Money, freedom, luxury
• Clear title and subheading
Nice to have
• Subtle dental reference
• dimensions 1600x2400
Should not have
• Boring photos of dentist/patients, dental clinic, teeth etc,

```html
<!DOCTYPE html>
<html lang="en">
<head>
<meta charset="utf-8">
<title>The Molar Compass — Ebook Cover</title>
<link href="https://fonts.googleapis.com/css2?family=Bebas+Neue&family=Montserrat:wght@300;500&display=swap" rel="stylesheet">
<style>
  :root {
    --page: #ffffff;
    --cover-dark: #0f0f0f;
    --cover-mid: #1e1e1e;
    --ink-light: #ffffff;
    --gold-light: #f3e39a;
    --gold-mid: #d9b24a;
    --gold-deep: #a87a1e;
  }
  html, body {
    margin: 0;
    padding: 0;
    width: 1200px;
    height: 1200px;
    overflow: hidden;
    background: var(--page);
  }
  .cover {
    position: absolute;
    left: 229px;
    top: 44px;
    width: 742px;
    height: 1112px;
    background: radial-gradient(ellipse at 50% 52%, var(--cover-mid) 0%, var(--cover-dark) 70%);
    color: var(--ink-light);
    text-align: center;
  }
  .title {
    margin: 0;
    font-family: "Bebas Neue", "Oswald", sans-serif;
    font-weight: 400;
    line-height: 1;
  }
  .title-top {
    position: absolute;
    left: 0;
    right: 0;
    top: 104px;
    font-size: 152px;
    letter-spacing: 2px;
    color: var(--ink-light);
  }
  .title-bottom {
    position: absolute;
    left: 0;
    right: 0;
    top: 242px;
    font-size: 164px;
    letter-spacing: 2px;
  }
  .title-bottom span {
    background: linear-gradient(90deg, var(--gold-mid) 0%, var(--gold-light) 40%, var(--gold-mid) 70%, var(--gold-deep) 100%);
    -webkit-background-clip: text;
    background-clip: text;
    color: transparent;
  }
  .subtitle {
    position: absolute;
    left: 0;
    right: 0;
    top: 436px;
    margin: 0;
    font-family: "Montserrat", sans-serif;
    font-weight: 500;
    font-size: 24px;
    line-height: 46px;
    letter-spacing: 4.5px;
    text-transform: uppercase;
  }
  .coin {
    position: absolute;
    left: 213px;
    top: 594px;
    width: 316px;
    height: 316px;
  }
  .author {
    position: absolute;
    left: 0;
    right: 0;
    top: 1020px;
    margin: 0;
    font-family: "Montserrat", sans-serif;
    font-weight: 300;
    font-size: 58px;
    letter-spacing: 18px;
    text-transform: uppercase;
    padding-left: 18px;
  }
</style>
</head>
<body>
  <main class="cover">
    <h1 class="title">
      <span class="title-top">The Molar</span>
      <span class="title-bottom"><span>Compass</span></span>
    </h1>
    <p class="subtitle">The secrets to money,<br>motivation and success</p>
    <svg class="coin" viewBox="0 0 316 316" role="img" aria-label="Gold coin emblem with a small tooth at its centre, ringed by stars">
      <defs>
        <linearGradient id="coinGold" x1="0" y1="0" x2="1" y2="1">
          <stop offset="0" stop-color="#c8952e"/>
          <stop offset="0.45" stop-color="#f1df92"/>
          <stop offset="1" stop-color="#b07f22"/>
        </linearGradient>
      </defs>
      <circle cx="158" cy="158" r="156" fill="url(#coinGold)"/>
    </svg>
    <p class="author">Kate Fenwick</p>
  </main>
</body>
</html>
```